Photographer Card

I'm currently doing freelance photography and i need a creative design name card especially when i attend events.
I require a design that makes a STATEMENT.
Simple, elegant and nothing like the usual name cards ive seen around (Example: with a camera/tripod etc in the design).

Photographer: Brent LW
Mobile: +65 91846257
E-mail: Brent.LW.Photography@mailvento.com
Facebook: www.friendspage.com/brent.lw.photography

Thanks for your time and hope it will turn out well! :)

Thanks for all your inputs!

Im liking the cursive feel.

Id prefer not to include the title "freelance"  :)

Also, im looking for a logo to establish myself

http://www.artnookgallery.com/art/Pebbles-Business-Card-506213847

Hi all! Thanks for the designs

"Capturing magical moments"
"Capturing magical moments that are gone forever"

Back design can be in big font "look HERE"

Maybe with focusing box 

Names can be played with horizontal and vertical.

Camera

Script

```html
<!DOCTYPE html>
<html lang="en">
<head>
<meta charset="utf-8">
<title>Brent LW – Photographer Card</title>
<link rel="stylesheet" href="https://fonts.googleapis.com/css2?family=Space+Mono&family=IBM+Plex+Mono:wght@300&family=Roboto+Condensed:wght@300&display=swap">
<style>
  :root {
    --paper: #ffffff;
    --ink: #111111;
    --name-band: #000000;
    --name-text: #ffffff;
    --photo-light: #bdbdbd;
    --photo-mid: #7a7a7a;
    --photo-dark: #1e1e1e;
  }
  html, body {
    margin: 0;
    padding: 0;
    overflow: hidden;
    background: var(--paper);
  }
  .card {
    position: relative;
    width: 1200px;
    height: 388px;
    background: var(--paper);
    color: var(--ink);
    overflow: hidden;
  }
  .tagline {
    position: absolute;
    left: 0;
    width: 600px;
    margin: 0;
    text-align: center;
    font-family: "Space Mono", monospace;
    font-size: 25px;
    line-height: 1;
    letter-spacing: 0.5px;
  }
  .tagline--top { top: 12px; }
  .tagline--bottom { top: 348px; }
  .portrait {
    position: absolute;
    left: 0;
    top: 54px;
    width: 600px;
    height: 286px;
    background:
      radial-gradient(ellipse 40% 60% at 45% 45%, var(--photo-light), transparent 70%),
      linear-gradient(90deg, var(--photo-dark) 0%, var(--photo-mid) 30%, var(--photo-mid) 70%, var(--photo-dark) 92%, var(--photo-light) 100%);
  }
  .identity {
    position: absolute;
    left: 630px;
    top: 66px;
  }
  .identity__name {
    display: inline-block;
    margin: 0;
    padding: 0 10px 0 8px;
    height: 60px;
    line-height: 60px;
    background: var(--name-band);
    color: var(--name-text);
    font-family: "IBM Plex Mono", monospace;
    font-weight: 300;
    font-size: 56px;
    letter-spacing: 1px;
  }
  .identity__role {
    margin: 8px 0 0 4px;
    font-family: "IBM Plex Mono", monospace;
    font-weight: 300;
    font-size: 42px;
    line-height: 1;
  }
  .contacts {
    position: absolute;
    left: 632px;
    top: 240px;
    margin: 0;
    padding: 0;
    list-style: none;
    font-family: "Roboto Condensed", sans-serif;
    font-weight: 300;
    font-size: 24px;
    line-height: 38px;
  }
</style>
</head>
<body>
  <main class="card">
    <p class="tagline tagline--top">“I’ll be watching you!”</p>
    <div class="portrait" role="img" aria-label="Black and white close-up portrait photograph of the photographer"></div>
    <p class="tagline tagline--bottom">It’s OK - I’m a photographer</p>

    <header class="identity">
      <h1 class="identity__name">Brent LW</h1>
      <p class="identity__role">Photographer</p>
    </header>

    <ul class="contacts">
      <li class="contacts__item">M: +65 91846257</li>
      <li class="contacts__item">E: Brent.LW.Photography@mailvento.com</li>
      <li class="contacts__item">F: www.friendspage.com/brent.lw.photography</li>
    </ul>
  </main>
</body>
</html>
```